Corvane Real Estate Business Card

hello, we are a real estate company located in Los Angeles, california. we are a boutique, small company but we like a big corportate look. a simple, sleek, modern and progressive look. we would like the option of having a design that could include the real estate agents personal photo and also a design if the realtor desides not to have a photo. We also would like a hotizontal design.

Corvane Properties
3817 S Hadderly
Larkfield, CA 90417
www.CorvaneRE.example

Gavin Prosk
Broker
BRE # 04829176
(555) 274-6390
gavin@corvanere.example

```html
<!DOCTYPE html>
<html lang="en">
<head>
<meta charset="utf-8">
<title>Corvane Real Estate Business Card</title>
<link rel="stylesheet" href="https://fonts.googleapis.com/css2?family=Questrial&family=Montserrat:wght@600&display=swap">
<style>
  :root {
    --page-bg: #2b2b2d;
    --blue-light: #4cc0f2;
    --blue-mid: #1f9be0;
    --blue-deep: #0f6fb8;
    --brand-navy: #1d4f8c;
    --band-dark: #2a2a2c;
    --band-darker: #1f1f21;
    --text-white: #ffffff;
    --text-soft: #e6e6e6;
    --rule: #6b6b6e;
  }
  * { margin: 0; padding: 0; box-sizing: border-box; }
  html, body {
    width: 1200px; height: 849px; overflow: hidden;
    background: var(--page-bg);
  }
  .stage {
    position: relative; width: 1200px; height: 849px;
    display: flex; align-items: center; justify-content: center;
  }
  .business-card {
    position: relative; width: 900px; height: 514px;
    border-radius: 22px; overflow: hidden;
    box-shadow: 0 18px 40px rgba(0,0,0,.45);
    font-family: "Questrial", "Century Gothic", sans-serif;
  }
  .card-top {
    position: absolute; left: 0; top: 0; width: 100%; height: 285px;
    background: radial-gradient(ellipse at 38% 55%, var(--blue-light) 0%, var(--blue-mid) 45%, var(--blue-deep) 100%);
  }
  .dot-field {
    position: absolute; right: 0; top: 0; width: 330px; height: 285px;
    background: radial-gradient(ellipse at 80% 45%, rgba(160,215,245,.55) 0%, rgba(120,195,240,.3) 45%, rgba(120,195,240,0) 80%);
  }
  .brand {
    position: absolute; left: 230px; top: 120px;
    display: flex; align-items: center; gap: 16px;
  }
  .brand-mark {
    width: 44px; height: 44px; border-radius: 50%;
    background: var(--brand-navy);
  }
  .brand-name {
    font-size: 74px; line-height: 1; color: var(--brand-navy);
    letter-spacing: -1px;
  }
  .card-bottom {
    position: absolute; left: 0; top: 285px; width: 100%; height: 229px;
    background: linear-gradient(180deg, var(--band-dark), var(--band-darker));
  }
  .agent {
    position: absolute; right: 470px; top: 315px; text-align: right;
    color: var(--text-white);
  }
  .agent-name {
    font-family: "Montserrat", "Century Gothic", sans-serif;
    font-weight: 600; font-size: 34px; line-height: 1.2;
  }
  .agent-title { font-size: 25px; color: var(--text-soft); margin-top: 6px; }
  .agent-title small { font-size: 20px; }
  .divider {
    position: absolute; left: 452px; top: 312px; width: 1px; height: 160px;
    background: var(--rule);
  }
  .contact-list {
    position: absolute; left: 478px; top: 318px; list-style: none;
    color: var(--text-white); font-size: 21px; white-space: nowrap;
  }
  .contact-list li {
    display: flex; align-items: center; gap: 12px; height: 35px;
  }
  .contact-icon { width: 20px; height: 20px; flex: none; }
</style>
</head>
<body>
<main class="stage">
  <article class="business-card">
    <section class="card-top">
      <div class="dot-field" role="img" aria-label="Decorative pattern of soft light-blue dots"></div>
      <div class="brand">
        <span class="brand-mark"></span>
        <span class="brand-name">corvane</span>
      </div>
    </section>

    <section class="card-bottom"></section>

    <div class="agent">
      <p class="agent-name">Gavin Prosk</p>
      <p class="agent-title">Broker, <small>BRE # 04829176</small></p>
    </div>

    <div class="divider"></div>

    <ul class="contact-list">
      <li>
        <svg class="contact-icon" viewBox="0 0 20 20" aria-hidden="true">
          <circle cx="10" cy="10" r="9" fill="none" stroke="#fff" stroke-width="1.4"/>
          <path d="M7 5.5 L8.6 5.5 L9.3 7.8 L8.2 8.7 Q9.2 10.9 11.3 11.8 L12.2 10.7 L14.5 11.4 L14.5 13 Q13.6 14.5 11.6 14 Q6.2 12.3 5.9 7.2 Q6 5.8 7 5.5Z" fill="#fff"/>
        </svg>
        <span>(555) 274-6390</span>
      </li>
      <li>
        <svg class="contact-icon" viewBox="0 0 20 20" aria-hidden="true">
          <circle cx="10" cy="10" r="9" fill="none" stroke="#fff" stroke-width="1.4"/>
          <rect x="5" y="6.5" width="10" height="7" fill="none" stroke="#fff" stroke-width="1.3"/>
          <path d="M5 6.8 L10 10.6 L15 6.8" fill="none" stroke="#fff" stroke-width="1.3"/>
        </svg>
        <span>gavin@corvanere.example</span>
      </li>
      <li>
        <svg class="contact-icon" viewBox="0 0 20 20" aria-hidden="true">
          <circle cx="10" cy="10" r="9" fill="none" stroke="#fff" stroke-width="1.4"/>
          <circle cx="10" cy="10" r="5" fill="none" stroke="#fff" stroke-width="1.2"/>
          <ellipse cx="10" cy="10" rx="2.2" ry="5" fill="none" stroke="#fff" stroke-width="1.1"/>
          <line x1="5" y1="10" x2="15" y2="10" stroke="#fff" stroke-width="1.1"/>
        </svg>
        <span>www.CorvaneRE.example</span>
      </li>
      <li>
        <svg class="contact-icon" viewBox="0 0 20 20" aria-hidden="true">
          <circle cx="10" cy="10" r="9" fill="none" stroke="#fff" stroke-width="1.4"/>
          <path d="M10 15.5 Q6 11 6 8.5 A4 4 0 0 1 14 8.5 Q14 11 10 15.5Z" fill="#fff"/>
          <circle cx="10" cy="8.5" r="1.5" fill="#2a2a2c"/>
        </svg>
        <span>3817 S Hadderly, Larkfield, CA 90417</span>
      </li>
    </ul>
  </article>
</main>
</body>
</html>
```